"Dental Kestrel" clinic needs brochure

a creative design is needed for flyer for a dental clinic, all info available on this website www.dentalkestrel.ae, new imagery needed.

Clinic

```html
<!DOCTYPE html>
<html lang="en">
<head>
<meta charset="utf-8">
<title>Dental Kestrel Clinic – Flyer</title>
<link href="https://fonts.googleapis.com/css2?family=PT+Sans:ital,wght@0,400;0,700;1,400&display=swap" rel="stylesheet">
<style>
  :root{
    --page:#ffffff;
    --teal-deep:#163f5a;
    --teal-mid:#1c5468;
    --teal-light:#1e6474;
    --brand:#1f6b6e;
    --frame:#1d5a68;
    --ink:#111111;
    --footer-ink:#222222;
    --white:#ffffff;
  }
  *{margin:0;padding:0;box-sizing:border-box}
  html,body{width:1200px;height:1200px;overflow:hidden;background:var(--page)}
  body{font-family:"PT Sans",sans-serif;color:var(--ink)}
  .flyer{position:absolute;left:200px;top:35px;width:800px;height:1130px;background:var(--white);overflow:hidden}
  .flyer-band,.flyer-photos{position:absolute;inset:0}
  .brand{position:absolute;top:92px;left:0;width:800px;display:flex;align-items:center;justify-content:center;gap:18px}
  .brand-dot{width:30px;height:30px;border-radius:50%;background:var(--brand)}
  .brand-name{font-weight:700;font-size:46px;letter-spacing:4px;color:var(--brand);text-transform:uppercase}
  .hours{position:absolute;left:47px;top:234px;font-weight:700;line-height:26px}
  .hours h2{font-size:23px;line-height:28px}
  .hours p{font-size:19px}
  .about{position:absolute;left:0;top:484px;width:747px;height:207px;background:rgba(15,45,65,.35);color:var(--white);padding-top:8px}
  .section-title{font-weight:700;font-size:29px;line-height:34px;color:var(--white)}
  .about .section-title{text-align:center;width:776px}
  .about p{width:800px;text-align:center;font-size:19px;line-height:25.7px;white-space:nowrap}
  .services{position:absolute;left:47px;top:697px;width:753px;height:369px;background:rgba(15,45,65,.25);color:var(--white)}
  .services .section-title{text-align:center;margin-top:6px;margin-left:-10px}
  .col{position:absolute;top:47px;list-style:none}
  .col-left{left:28px}
  .col-right{left:331px;top:49px;width:400px}
  .col h3{font-weight:700;font-size:22px;line-height:28px}
  .col li{font-size:19.5px;line-height:26px;position:relative}
  .col li.item::before{content:"";position:absolute;left:-15px;top:11px;width:6px;height:6px;border-radius:50%;background:var(--white)}
  .footer{position:absolute;left:0;top:1066px;width:800px;height:64px;font-style:italic;font-size:17px;color:var(--footer-ink);text-align:center}
  .footer .line{display:flex;justify-content:center;align-items:center;gap:6px;height:25px;margin-top:7px}
  .footer .line + .line{margin-top:0;gap:90px}
  .footer .contact{display:flex;align-items:center;gap:6px}
</style>
</head>
<body>
<div class="flyer">
  <svg class="flyer-band" width="800" height="1130" viewBox="0 0 800 1130" aria-hidden="true">
    <defs>
      <linearGradient id="band" x1="0" y1="0" x2="0" y2="1">
        <stop offset="0" stop-color="#163f5a"/>
        <stop offset="1" stop-color="#1e6474"/>
      </linearGradient>
    </defs>
    <path d="M0,413 Q420,470 800,204 L800,1066 L0,1066 Z" fill="url(#band)"/>
  </svg>

  <header class="brand">
    <span class="brand-dot"></span>
    <span class="brand-name">Dental Kestrel Clinic</span>
  </header>

  <section class="hours">
    <h2>OPENING HOURS</h2>
    <p>Saturday - Sunday 11AM - 8PM</p>
    <p>Thursday - 11AM - 4PM</p>
  </section>

  <section class="about">
    <h2 class="section-title">ABOUT US</h2>
    <p>We are dental practice devoted to restoring and enhancing the natural<br>beauty of your smile using conservative, state-of-the-art procedures that will<br>result in beautiful, long lasting smiles.<br>A standard of excellence in personalized dental care services our patient de-<br>serve. We provide comprehensive treatment planning and use restorative<br>and cosmetic dentistry to achieve your optimal dental health.</p>
  </section>

  <svg class="flyer-photos" width="800" height="1130" viewBox="0 0 800 1130">
    <defs>
      <linearGradient id="photoSkin" x1="0" y1="0" x2="1" y2="1">
        <stop offset="0" stop-color="#f3d6cc"/>
        <stop offset="0.55" stop-color="#e9a79c"/>
        <stop offset="1" stop-color="#f6e4de"/>
      </linearGradient>
      <linearGradient id="photoExam" x1="0" y1="0" x2="1" y2="1">
        <stop offset="0" stop-color="#e8c2b6"/>
        <stop offset="0.5" stop-color="#d9675e"/>
        <stop offset="1" stop-color="#f0c9bd"/>
      </linearGradient>
    </defs>
    <g role="img" aria-label="Photo: close-up of an open smiling mouth">
      <polygon points="262.4,383.7 215.3,336.6 148.7,336.6 101.6,383.7 101.6,450.3 148.7,497.4 215.3,497.4 262.4,450.3" fill="url(#photoSkin)" stroke="#1d5a68" stroke-width="5"/>
    </g>
    <g role="img" aria-label="Photo: dental mirror during a check-up">
      <polygon points="468.4,332.7 414.3,278.6 337.7,278.6 283.6,332.7 283.6,409.3 337.7,463.4 414.3,463.4 468.4,409.3" fill="url(#photoExam)" stroke="#1d5a68" stroke-width="5"/>
    </g>
    <g role="img" aria-label="Photo: bright white smile close-up">
      <polygon points="693.4,266.7 632.3,205.6 545.7,205.6 484.6,266.7 484.6,353.3 545.7,414.4 632.3,414.4 693.4,353.3" fill="url(#photoSkin)" stroke="#1d5a68" stroke-width="5"/>
    </g>
  </svg>

  <section class="services">
    <h2 class="section-title">OUR SERVICES</h2>
    <ul class="col col-left">
      <li><h3>General Dentistry</h3></li>
      <li class="item">Scaling and Polishing</li>
      <li class="item">White fillings</li>
      <li class="item">Root canal treatment</li>
      <li class="item">Extraction</li>
      <li class="item">Inlays and Onlays</li>
      <li class="item">Surgical Removal Teeth</li>
      <li><h3>Cosmetic Dentistry</h3></li>
      <li class="item">Vaneerd (Hollywood smile)</li>
      <li class="item">Smile design</li>
      <li class="item">Ceramic Crowns</li>
      <li class="item">Laser Bleaching</li>
    </ul>
    <ul class="col col-right">
      <li><h3>Pediatric Dentistry</h3></li>
      <li class="item">White fillings</li>
      <li class="item">Flouride treatment</li>
      <li class="item">Pulpotomy and pulpectomy</li>
      <li class="item">Extraction</li>
      <li class="item">Special maintainer and Zircon crowns</li>
      <li><h3>Emergency Dentistry</h3></li>
      <li><h3>Biological Dentistry</h3></li>
      <li class="item">Safe Removal of Amalgam Fill-<br>ing(SMART)</li>
      <li class="item">Note: All our materials are Bio-com-<br>patible materials</li>
    </ul>
  </section>

  <footer class="footer">
    <div class="line">
      <svg width="12" height="16" viewBox="0 0 12 16" aria-hidden="true"><path d="M6 0C2.7 0 0 2.6 0 5.9 0 10.3 6 16 6 16s6-5.7 6-10.1C12 2.6 9.3 0 6 0zm0 8.3A2.4 2.4 0 1 1 6 3.5a2.4 2.4 0 0 1 0 4.8z" fill="#222"/></svg>
      <span>Suite 210, Corniche Garden Road, Opp Marina Park, Abu Dhabi.</span>
    </div>
    <div class="line">
      <span class="contact"><svg width="20" height="14" viewBox="0 0 20 14" aria-hidden="true"><path d="M1 4c0-2 4-3 9-3s9 1 9 3v2h-5V4H6v2H1zM5 7h10l3 6H2z" fill="#222"/></svg>+971 2 555 0187</span>
      <span>@dentalkestrel</span>
    </div>
  </footer>
</div>
</body>
</html>
```